Bref créative
Corvale Power Associates, LLC
Stationery and business cards
Professional
Dean Halvorsen
President
28715 Birchwood Crest Lane
Suite 615
Brenford, TX 75290
dean.halvorsen@corvale-pa.com
We will need multiple name, cell phone, and email changes. Primary colors should be white, black, and a vibrant blue.
Here is our logo Ai.

```html
<!DOCTYPE html>
<html lang="en">
<head>
<meta charset="utf-8">
<title>Corvale Power Associates — Stationery</title>
<link href="https://fonts.googleapis.com/css2?family=Open+Sans:wght@400;600;700&display=swap" rel="stylesheet">
<style>
  :root{
    --blue:#1d6fd6;
    --blue-deep:#0f4fae;
    --blue-light:#3f97f0;
    --black:#1b1b1b;
    --ink:#4a4a4a;
    --paper:#ffffff;
    --backdrop:#e9e7e3;
    --fold:#d9d9d9;
  }
  *{box-sizing:border-box;margin:0;padding:0}
  html,body{width:1200px;height:809px;overflow:hidden}
  body{background:var(--backdrop);font-family:"Open Sans",Arial,sans-serif;color:var(--ink);position:relative}
  .sheet{position:absolute;background:var(--paper);box-shadow:0 2px 8px rgba(0,0,0,.15);overflow:hidden}
  .sheet svg.swoosh{position:absolute;left:0;top:0;width:100%;height:100%}
  .brand{display:flex;align-items:center;gap:6px;font-weight:700;color:var(--blue);position:relative}
  .brand .dot{border-radius:50%;background:var(--blue);flex:none}
  .brand.on-blue{color:#fff}
  .brand.on-blue .dot{background:#fff}

  /* Letterhead */
  .letterhead{left:40px;top:100px;width:470px;height:608px}
  .letterhead .brand{position:absolute;left:38px;top:40px;font-size:18px}
  .letterhead .brand .dot{width:14px;height:14px}
  .letter{position:absolute;left:38px;top:105px;width:380px;font-size:6.4px;line-height:1.6}
  .letter .recipient{margin:10px 0 14px}
  .letter p{margin-bottom:8px}
  .letter .closing{margin-top:22px}
  .letter .signer{margin-top:18px}
  .letterhead .footer{position:absolute;left:38px;bottom:28px;font-size:6px;line-height:1.5}

  /* Envelope front */
  .envelope{left:540px;top:30px;width:600px;height:261px}
  .envelope .brand{position:absolute;left:28px;top:24px;font-size:17px}
  .envelope .brand .dot{width:13px;height:13px}
  .envelope .return{position:absolute;left:28px;top:150px;font-size:7px;line-height:1.5;color:var(--blue-deep)}

  /* Envelope back */
  .envelope-back{left:540px;top:311px;width:600px;height:261px}
  .envelope-back .brand{position:absolute;left:0;right:0;top:50px;justify-content:center;font-size:17px}
  .envelope-back .brand .dot{width:13px;height:13px}

  /* Business cards */
  .card{top:596px;width:290px;height:166px;border-radius:3px}
  .card-front{left:540px}
  .card-front .brand{position:absolute;left:18px;top:18px;font-size:13px}
  .card-front .brand .dot{width:10px;height:10px}
  .card-front .person{position:absolute;left:18px;top:88px;font-size:7px;line-height:1.5}
  .card-front .person .name{font-weight:700;color:var(--blue-deep);font-size:8px}
  .card-front .contact{position:absolute;left:110px;top:88px;font-size:6px;line-height:1.55}
  .card-back{left:850px;background:linear-gradient(135deg,var(--blue-light),var(--blue-deep))}
  .card-back .brand{position:absolute;left:0;right:0;top:70px;justify-content:center;font-size:17px}
  .card-back .brand .dot{width:13px;height:13px}
</style>
</head>
<body>

<section class="sheet letterhead" aria-label="Letterhead">
  <svg class="swoosh" viewBox="0 0 470 608" preserveAspectRatio="none" aria-hidden="true">
    <path d="M150,608 C290,600 420,560 470,470 L470,608Z" fill="var(--black)"/>
    <path d="M200,608 C320,600 430,572 470,495 L470,608Z" fill="var(--blue)"/>
  </svg>
  <div class="brand"><span class="dot"></span>Corvale</div>
  <div class="letter">
    <div>Date</div>
    <div class="recipient">Recipient Name<br>Title<br>Company Name<br>City, State ZIP</div>
    <p>Dear Mr. Ellery,</p>
    <p>Thank you for meeting with our team last week to review the pipeline expansion plans. We appreciate your time and the detailed questions raised during the site visit.</p>
    <p>Our engineers have prepared a revised schedule covering permits, materials and field crews for the coming quarter. The attached summary outlines each phase and the expected costs.</p>
    <p>Please let us know if you would like to arrange a follow-up call. We look forward to working with you on this project.</p>
    <div class="closing">Sincerely,</div>
    <div class="signer">Dean Halvorsen</div>
  </div>
  <div class="footer">28715 Birchwood Crest Lane Suite 615 Brenford, TX 75290<br>P: 555.555.0142 &nbsp;|&nbsp; dean.halvorsen@corvale-pa.com</div>
</section>

<section class="sheet envelope" aria-label="Envelope front">
  <svg class="swoosh" viewBox="0 0 600 261" preserveAspectRatio="none" aria-hidden="true">
    <path d="M395,0 C470,60 515,170 510,261 L600,261 L600,0Z" fill="var(--black)"/>
    <path d="M420,0 C495,60 540,170 535,261 L600,261 L600,0Z" fill="var(--blue)"/>
  </svg>
  <div class="brand"><span class="dot"></span>Corvale</div>
  <div class="return">If not delivered please return to:<br>28715 Birchwood Crest Lane Suite 615 Brenford, TX 75290<br>P: 555.555.0142</div>
</section>

<section class="sheet envelope-back" aria-label="Envelope back">
  <svg class="swoosh" viewBox="0 0 600 261" preserveAspectRatio="none" aria-hidden="true">
    <defs>
      <linearGradient id="flap" x1="0" y1="0" x2="1" y2="0">
        <stop offset="0" stop-color="var(--blue-deep)"/>
        <stop offset=".5" stop-color="var(--blue-light)"/>
        <stop offset="1" stop-color="var(--blue-deep)"/>
      </linearGradient>
    </defs>
    <path d="M0,261 L285,150 Q300,144 315,150 L600,261" fill="none" stroke="var(--fold)" stroke-width="1.5"/>
    <path d="M0,0 H600 V30 L330,130 Q300,142 270,130 L0,30Z" fill="url(#flap)"/>
  </svg>
  <div class="brand on-blue"><span class="dot"></span>Corvale</div>
</section>

<section class="sheet card card-front" aria-label="Business card front">
  <svg class="swoosh" viewBox="0 0 290 166" preserveAspectRatio="none" aria-hidden="true">
    <path d="M205,0 C240,40 258,110 250,166 L290,166 L290,0Z" fill="var(--black)"/>
    <path d="M218,0 C252,40 270,110 262,166 L290,166 L290,0Z" fill="var(--blue)"/>
  </svg>
  <div class="brand"><span class="dot"></span>Corvale</div>
  <div class="person"><div class="name">Dean Halvorsen</div><div>President</div></div>
  <div class="contact">28715 Birchwood Crest Lane<br>Suite 615<br>Brenford, TX 75290<br>P: 555.555.0142<br>F: 555.555.0199<br>dean.halvorsen@corvale-pa.com</div>
</section>

<section class="sheet card card-back" aria-label="Business card back">
  <div class="brand on-blue"><span class="dot"></span>Corvale</div>
</section>

</body>
</html>
```